First Aid Training business needs business card design

We would like a double sided business card designed for a first aid training business - Brindlewood First Aid. We provide first aid training and , WHS (work, health and safety) training.

The attached word document contains the key information we would like on each side of the business card.

Final design needs to be delivered in print ready format, along with the original file.

```html
<!DOCTYPE html>
<html lang="en">
<head>
<meta charset="utf-8">
<title>Brindlewood First Aid – Business Card</title>
<link href="https://fonts.googleapis.com/css2?family=Montserrat:wght@400;500;600;700&display=swap" rel="stylesheet">
<style>
  :root {
    --red: #ec0000;
    --grey: #7f7f7f;
    --ink: #1f1f1f;
    --arc: #262626;
    --paper: #f6f6f6;
    --white: #ffffff;
    --stage: #e4e4e4;
  }
  * { box-sizing: border-box; margin: 0; padding: 0; }
  html, body { width: 1200px; height: 900px; overflow: hidden; }
  body {
    background: var(--stage);
    font-family: "Montserrat", sans-serif;
    display: flex;
    flex-direction: column;
    align-items: center;
    justify-content: center;
    gap: 60px;
  }
  .card {
    position: relative;
    width: 560px;
    height: 320px;
    background: var(--paper);
    overflow: hidden;
    box-shadow: 0 6px 18px rgba(0,0,0,.18);
  }

  /* Front */
  .front-shapes { position: absolute; inset: 0; }
  .holder-name {
    position: absolute;
    left: 70px; top: 56px;
    color: var(--red);
    font-weight: 600;
    font-size: 22px;
    letter-spacing: .5px;
  }
  .holder-rule {
    position: absolute;
    left: 66px; top: 90px;
    width: 150px; height: 1px;
    background: linear-gradient(90deg, rgba(255,255,255,.9), rgba(255,255,255,0));
  }
  .contact-tab {
    position: absolute;
    left: 0; top: 168px;
    width: 58px; height: 96px;
    background: var(--red);
    border-radius: 0 10px 10px 0;
    display: flex; flex-direction: column; justify-content: space-around; align-items: center;
    padding: 8px 0 8px 16px;
  }
  .contact-tab svg { width: 16px; height: 16px; }
  .contact-list {
    position: absolute;
    left: 76px; top: 176px;
    list-style: none;
    color: var(--white);
    font-size: 12.5px;
    line-height: 29px;
    letter-spacing: .3px;
  }
  .brand-front {
    position: absolute;
    right: 18px; top: 34px;
    width: 150px;
    display: flex; flex-direction: column; align-items: center; gap: 10px;
  }
  .brand-dot { width: 42px; height: 42px; border-radius: 50%; background: var(--red); }
  .brand-name {
    color: var(--ink);
    font-weight: 700;
    font-size: 15px;
    line-height: 1.2;
    text-align: center;
    letter-spacing: .4px;
  }

  /* Back */
  .back-content {
    position: absolute;
    inset: 0 0 60px 0;
    display: flex; flex-direction: column; align-items: center;
    padding-top: 46px;
    color: var(--ink);
  }
  .offer-title {
    font-weight: 500;
    font-size: 17px;
    padding-bottom: 5px;
    border-bottom: 1.5px solid var(--ink);
    letter-spacing: .3px;
  }
  .benefits {
    list-style: none;
    margin-top: 10px;
    text-align: center;
    font-weight: 600;
    font-size: 18px;
    line-height: 25px;
  }
  .benefits li::before {
    content: "";
    display: inline-block;
    width: 7px; height: 7px;
    background: var(--red);
    border: 1.5px solid var(--ink);
    margin-right: 10px;
    vertical-align: middle;
  }
  .brand-back {
    margin-top: 22px;
    display: flex; align-items: center; gap: 10px;
  }
  .brand-back .brand-dot { width: 34px; height: 34px; background: var(--ink); }
  .brand-back .brand-name { font-size: 15px; text-align: left; }
  .service-band {
    position: absolute;
    left: 0; right: 0; bottom: 0;
    height: 42px;
    background: var(--red);
  }
  .service-tabs {
    position: absolute;
    left: 100px; right: 100px; bottom: 20px;
    height: 56px;
    background: var(--red);
    border-radius: 6px 6px 0 0;
    display: flex; align-items: center;
    color: var(--white);
    font-weight: 600;
    font-size: 17px;
  }
  .service { flex: 1; text-align: center; }
  .service-divider { width: 1.5px; height: 32px; background: var(--white); }
</style>
</head>
<body>

  <section class="card card-front" aria-label="Business card front">
    <svg class="front-shapes" viewBox="0 0 560 320" width="560" height="320" aria-hidden="true">
      <circle cx="10" cy="334" r="423" fill="none" stroke="var(--arc)" stroke-width="18"/>
      <circle cx="10" cy="334" r="407" fill="none" stroke="var(--white)" stroke-width="14"/>
      <circle cx="10" cy="334" r="400" fill="var(--grey)"/>
      <rect x="0" y="0" width="20" height="320" fill="var(--red)"/>
    </svg>

    <p class="holder-name">Daniel Harper</p>
    <div class="holder-rule"></div>

    <div class="contact-tab" aria-hidden="true">
      <svg viewBox="0 0 24 24"><path d="M6.6 10.8a15 15 0 0 0 6.6 6.6l2.2-2.2c.3-.3.7-.4 1-.2 1.1.4 2.3.6 3.6.6.6 0 1 .4 1 1V20c0 .6-.4 1-1 1C10.6 21 3 13.4 3 4c0-.6.4-1 1-1h3.5c.6 0 1 .4 1 1 0 1.3.2 2.5.6 3.6.1.3 0 .7-.2 1z" fill="var(--white)"/></svg>
      <svg viewBox="0 0 24 24"><rect x="3" y="6" width="18" height="13" rx="1.5" fill="none" stroke="var(--white)" stroke-width="2"/><path d="M3.5 7 12 13l8.5-6" fill="none" stroke="var(--white)" stroke-width="2"/></svg>
      <svg viewBox="0 0 24 24"><circle cx="12" cy="12" r="9" fill="none" stroke="var(--white)" stroke-width="1.8"/><path d="M3 12h18M12 3c3 3 3 15 0 18M12 3c-3 3-3 15 0 18" fill="none" stroke="var(--white)" stroke-width="1.6"/></svg>
    </div>
    <ul class="contact-list">
      <li>0412 555 086</li>
      <li>help@brindlewoodfirstaid.com.au</li>
      <li>brindlewoodfirstaid.com.au</li>
    </ul>

    <div class="brand-front">
      <span class="brand-dot" aria-hidden="true"></span>
      <p class="brand-name">BRINDLEWOOD<br>FIRST AID</p>
    </div>
  </section>

  <section class="card card-back" aria-label="Business card back">
    <div class="back-content">
      <h2 class="offer-title">Onsite Training – We can come to you</h2>
      <ul class="benefits">
        <li>Time efficient</li>
        <li>Cost effective</li>
        <li>Minimise downtime for your team</li>
      </ul>
      <div class="brand-back">
        <span class="brand-dot" aria-hidden="true"></span>
        <p class="brand-name">BRINDLEWOOD<br>FIRST AID</p>
      </div>
    </div>
    <div class="service-band"></div>
    <div class="service-tabs">
      <span class="service">First Aid Training</span>
      <span class="service-divider" aria-hidden="true"></span>
      <span class="service">WHS Training</span>
    </div>
  </section>

</body>
</html>
```